QRD Mortgage Flyer

We are a mortgage company, advertising for he QRD streamline program. I would like the following information to be included on the post card:
Most of this information should be on one side of the card
LOWER YOUR QRD MORTGAGE PAYMENT RIGHT NOW

Using the QRD Streamline program you might be eligible to lower your interest rate and monthly mortgage insurance (MIP) at zero cost to you
The QRD has dramatically reduced its restrictions on Mortgage Insurance Premiums (MIP), combined with rates at historic lows, now is the time to take advantage of the QRD Streamline Program.

The Streamline process requires NO APPRAISAL, NO INCOME VERIFICATION, NO ASSET DOCUMENTATION and NO OUT OF POCKET CLOSING COSTS.
What this means to you is:
A REDUCTION IN MONTHLY PAYMENT
POSSIBILITY TO SKIP FIRST TWO MORTGAGE PAYMENTS
SAME TYPE OF 30 YEAR FIXED RATE LOAN – BACKED BY THE QRD
*To qualify for the QRD STREAMLINE you must have a good payment history with zero late payments in the past 12 months

I would like to include our logos on both sides, one side should have the KTV logo as well.
Please have our contact info displayed prominently on both sides
the contact information is as follows and all must be included

Pinewell Mortgage
418 Dorrance Avenue, Suite 1513
Seattle, WA 98163
Office 206 555 0148
Fax 206 555 0192
Email streamline@pinewellmortgage-example.net
Tom Halvorsen - Vice President - MLO-41937
Dev Okafor - Loan Originator

If you could please make the postcard colorful as well as adding some appropriate artwork (home, fence, yard etc) that would be great
thanks so much

```html
<!DOCTYPE html>
<html lang="en">
<head>
<meta charset="utf-8">
<title>QRD Streamline Postcard – Pinewell Mortgage</title>
<link rel="stylesheet" href="https://fonts.googleapis.com/css2?family=Roboto+Condensed:wght@300;400;700&display=swap">
<style>
  :root {
    --green-dark: #2c6a2e;
    --green: #3d7f35;
    --yellow: #fbd35c;
    --gray-title: #8c8c8c;
    --gray-panel-light: #e6e6e6;
    --gray-panel-dark: #a9a9a9;
    --brown: #87430f;
    --ink: #1e1e1e;
    --red: #e0262c;
    --tick: #4aa63a;
    --white: #ffffff;
  }
  html, body { margin: 0; padding: 0; overflow: hidden; background: var(--white); }
  .postcard {
    position: relative; width: 1200px; height: 773px; overflow: hidden;
    background: var(--white);
    font-family: "Roboto Condensed", "Arial Narrow", sans-serif; color: var(--ink);
  }
  .backdrop, .hero-photo { position: absolute; left: 0; top: 0; }
  .text { position: absolute; margin: 0; white-space: nowrap; }

  .headline-lead { left: 24px; top: 22px; font-size: 54px; font-weight: 400; color: var(--gray-title); line-height: 1; }
  .headline-main { left: 24px; top: 90px; font-size: 44px; font-weight: 700; color: var(--green-dark); line-height: 1; }
  .headline-main span { font-weight: 400; color: var(--gray-title); }

  .intro { left: 24px; top: 161px; font-size: 23px; line-height: 32px; color: #3b3520; }
  .intro strong { color: #5a3a0c; }

  .pitch { left: 28px; top: 243px; font-size: 23px; line-height: 32px; color: var(--white); }
  .pitch strong { font-size: 26.5px; line-height: 40px; }

  .requires-title { left: 19px; top: 374px; font-size: 23px; }
  .requires-list, .benefits-list { position: absolute; margin: 0; padding: 0; list-style: none; }
  .requires-list { left: 22px; top: 410px; }
  .requires-list li { display: flex; align-items: center; height: 43px; font-size: 26px; font-weight: 700; }
  .requires-list svg { width: 24px; height: 24px; margin-right: 12px; flex: none; }

  .benefits-title { left: 423px; top: 374px; font-size: 24px; }
  .benefits-list { left: 414px; top: 410px; }
  .benefits-list li { position: relative; display: flex; align-items: center; height: 42px; font-size: 26.5px; font-weight: 700; color: var(--brown); white-space: nowrap; }
  .benefits-list svg { width: 26px; height: 26px; margin-right: 16px; flex: none; }
  .benefits-list li:nth-child(2) { margin-left: 24px; }
  .benefits-list li:nth-child(3) { margin-left: 51px; }
  .benefits-list .continued { position: absolute; left: 68px; top: 37px; }

  .footnote { left: 701px; top: 591px; font-size: 18px; line-height: 23px; color: #222; }

  .brand-box {
    position: absolute; left: 42px; top: 630px; width: 190px; height: 124px;
    background: var(--white); display: flex; align-items: center; justify-content: center; gap: 8px;
  }
  .brand-box .dot { width: 14px; height: 14px; border-radius: 50%; background: var(--green); }
  .brand-box .brand-name { font-size: 25px; font-weight: 700; color: var(--green-dark); text-align: center; line-height: 1.05; }

  .contact { left: 260px; top: 640px; color: var(--white); font-size: 19px; line-height: 29px; font-style: normal; }
  .contact .company { font-size: 22px; font-weight: 700; }

  .officer { position: absolute; top: 667px; line-height: 1; white-space: nowrap; }
  .officer .name { font-size: 28px; font-weight: 700; display: block; }
  .officer .role { font-size: 21px; display: block; margin-top: 8px; }
  .officer .role small { font-size: 18px; }
  .officer-vp { left: 722px; }
  .officer-vp .role { margin-left: 17px; }
  .officer-lo { left: 1002px; }
  .officer-lo .role { margin-left: 28px; }
</style>
</head>
<body>
<main class="postcard">

  <svg class="backdrop" width="1200" height="773" viewBox="0 0 1200 773" aria-hidden="true">
    <defs>
      <linearGradient id="panel-gray" x1="0" y1="0" x2="1" y2="1">
        <stop offset="0" stop-color="var(--gray-panel-light)"/>
        <stop offset="1" stop-color="var(--gray-panel-dark)"/>
      </linearGradient>
      <linearGradient id="footer-gray" x1="0" y1="0" x2="0" y2="1">
        <stop offset="0" stop-color="#e4e4e4"/>
        <stop offset="1" stop-color="#c6c6c6"/>
      </linearGradient>
    </defs>
    <rect class="intro-band" x="0" y="154" width="760" height="78" fill="var(--yellow)"/>
    <polygon class="pitch-band" points="0,232 748,232 800,349 0,349" fill="var(--green-dark)"/>
    <polygon class="requires-panel" points="0,358 384,358 526,598 0,598" fill="url(#panel-gray)"/>
    <polygon class="footer-band" points="0,630 656,630 668,650 1200,650 1200,773 0,773" fill="var(--green-dark)"/>
    <polygon class="footer-names" points="668,650 1200,650 1200,752 748,752" fill="url(#footer-gray)"/>
    <line x1="956" y1="658" x2="1022" y2="748" stroke="#222" stroke-width="2"/>
  </svg>

  <svg class="hero-photo" width="1200" height="400" viewBox="0 0 1200 400" role="img" aria-label="Photo of a smiling couple sitting on the lawn in front of a yellow house with a tiled roof">
    <defs>
      <linearGradient id="photo-tones" x1="0" y1="0" x2="0" y2="1">
        <stop offset="0" stop-color="#c9a071"/>
        <stop offset="0.3" stop-color="#e8c13e"/>
        <stop offset="0.6" stop-color="#8fb060"/>
        <stop offset="1" stop-color="#4f8a2c"/>
      </linearGradient>
    </defs>
    <path d="M700 0 L1200 0 L1200 392 C1060 392 860 330 760 230 C712 170 698 90 700 0 Z" fill="var(--green-dark)"/>
    <path d="M708 0 L1200 0 L1200 372 C1060 376 866 318 770 222 C722 164 706 86 708 0 Z" fill="url(#photo-tones)"/>
  </svg>

  <p class="text headline-lead">Lower Your</p>
  <h1 class="text headline-main">QRD MORTGAGE PAYMENT <span>Right Now</span></h1>

  <p class="text intro">Using the QRD Streamline program you might be eligible to lower<br>your interest rate and monthly <strong>Mortgage Insurance (MIP) at zero cost</strong> to you.</p>

  <p class="text pitch">The QRD has dramatically reduced its restrictions on<br>Mortgage Insurance Premiums (MIP), combined with rates at historic lows,<br><strong>now is the time to take advantage of the QRD Streamline Program.</strong></p>

  <p class="text requires-title">The Streamline process requires</p>
  <ul class="requires-list">
    <li><svg viewBox="0 0 24 24"><circle cx="12" cy="12" r="11" fill="var(--white)" stroke="var(--red)" stroke-width="2"/><circle cx="12" cy="12" r="8" fill="var(--red)"/><path d="M8.8 8.8l6.4 6.4M15.2 8.8l-6.4 6.4" stroke="var(--white)" stroke-width="2.2" stroke-linecap="round"/></svg>NO APPRAISAL</li>
    <li><svg viewBox="0 0 24 24"><circle cx="12" cy="12" r="11" fill="var(--white)" stroke="var(--red)" stroke-width="2"/><circle cx="12" cy="12" r="8" fill="var(--red)"/><path d="M8.8 8.8l6.4 6.4M15.2 8.8l-6.4 6.4" stroke="var(--white)" stroke-width="2.2" stroke-linecap="round"/></svg>NO INCOME VERIFICATION</li>
    <li><svg viewBox="0 0 24 24"><circle cx="12" cy="12" r="11" fill="var(--white)" stroke="var(--red)" stroke-width="2"/><circle cx="12" cy="12" r="8" fill="var(--red)"/><path d="M8.8 8.8l6.4 6.4M15.2 8.8l-6.4 6.4" stroke="var(--white)" stroke-width="2.2" stroke-linecap="round"/></svg>NO ASSET DOCUMENTATION and</li>
    <li><svg viewBox="0 0 24 24"><circle cx="12" cy="12" r="11" fill="var(--white)" stroke="var(--red)" stroke-width="2"/><circle cx="12" cy="12" r="8" fill="var(--red)"/><path d="M8.8 8.8l6.4 6.4M15.2 8.8l-6.4 6.4" stroke="var(--white)" stroke-width="2.2" stroke-linecap="round"/></svg>NO OUT OF POCKET CLOSING COSTS.</li>
  </ul>

  <p class="text benefits-title">What this means to you is:</p>
  <ul class="benefits-list">
    <li><svg viewBox="0 0 26 26"><circle cx="13" cy="13" r="12" fill="var(--white)" stroke="var(--tick)" stroke-width="2"/><circle cx="13" cy="13" r="9" fill="var(--tick)"/><path d="M8.5 13.3l3.2 3.2 6-6.4" fill="none" stroke="var(--white)" stroke-width="2.4" stroke-linecap="round" stroke-linejoin="round"/></svg>A REDUCTION IN MONTHLY PAYMENT</li>
    <li><svg viewBox="0 0 26 26"><circle cx="13" cy="13" r="12" fill="var(--white)" stroke="var(--tick)" stroke-width="2"/><circle cx="13" cy="13" r="9" fill="var(--tick)"/><path d="M8.5 13.3l3.2 3.2 6-6.4" fill="none" stroke="var(--white)" stroke-width="2.4" stroke-linecap="round" stroke-linejoin="round"/></svg>POSSIBILITY TO SKIP FIRST TWO MORTGAGE PAYMENTS</li>
    <li><svg viewBox="0 0 26 26"><circle cx="13" cy="13" r="12" fill="var(--white)" stroke="var(--tick)" stroke-width="2"/><circle cx="13" cy="13" r="9" fill="var(--tick)"/><path d="M8.5 13.3l3.2 3.2 6-6.4" fill="none" stroke="var(--white)" stroke-width="2.4" stroke-linecap="round" stroke-linejoin="round"/></svg>SAME TYPE OF 30 YEAR FIXED RATE LOAN<span class="continued">- BACKED BY THE QRD</span></li>
  </ul>

  <p class="text footnote">*To qualify for the QRD STREAMLINE you must have a good<br>payment history with zero late payments in the past 12 months</p>

  <div class="brand-box">
    <span class="dot"></span>
    <span class="brand-name">Pinewell<br>Mortgage</span>
  </div>

  <address class="text contact">
    <span class="company">Pinewell Mortgage</span><br>
    418 Dorrance Avenue, Suite 1513, Seattle, WA 98163<br>
    Office: 206 555 0148 &nbsp;|&nbsp; Fax: 206 555 0192<br>
    Email: streamline@pinewellmortgage-example.net
  </address>

  <div class="officer officer-vp">
    <span class="name">Tom Halvorsen</span>
    <span class="role">Vice President - <small>MLO-41937</small></span>
  </div>
  <div class="officer officer-lo">
    <span class="name">Dev Okafor</span>
    <span class="role">Loan Originator</span>
  </div>

</main>
</body>
</html>
```